Website Banner Ad Design - 4x 200x200px panels that will rotate

I'm looking for four (4) 200x200px "panels" that will rotate on a website. Each one should have a unique description or key words on it, that makes it attractive to customers. It is important that each individual one kinda fits to our logo design to give it a "uniform" design.
The first panel should just be our logo and a slogan that says "AFFORDABLE. ACCELERATED. EFFECTIVE." This panel should also list our website "www.torvenix.com"
The second panel should have the following key text:
- Accelerated Training Courses
- Private Pilot in 4-weeks
- Career Programs from PPL to CFII
- Pay-as-you-go
The third panel should have the following key text:
- Advanced Training
- Firefighting (QPRA) & Forestry Tactics Training
- KX 310 & Tarn 118K Turbine Transition Training
- External-Load (VR) Courses
THE fourth panel should list our website address "www.torvenix.com" and phone number: (555) 482-7093.
I give free hand with the design. Any idea is welcome. See attached some photos and logo that can be used. If you visit http://www.quillmarshpost.com/FLIGHTTRAINING/tabid/421/Default.aspx you can see other 200x200 panels to get an idea of what we're looking for. Our look has to be professional and stick out from the rest of our competitors. By questions, just PM me.

```html
<!DOCTYPE html>
<html lang="en">
<head>
<meta charset="utf-8">
<title>Torvenix Banners</title>
<link rel="stylesheet" href="https://fonts.googleapis.com/css2?family=Roboto:wght@400;500&family=Roboto+Slab:wght@400;700&family=Open+Sans:wght@400&family=Lato:wght@400&display=swap">
<style>
  :root {
    --brand-blue: #1077bf;
    --deep-blue: #0d66a8;
    --stage: #4b4b4b;
    --stage-light: #565656;
    --ink-grey: #555555;
    --white: #ffffff;
  }
  * { margin: 0; padding: 0; box-sizing: border-box; }
  html, body { width: 1200px; height: 1200px; overflow: hidden; }
  body {
    position: relative;
    background: radial-gradient(circle at 50% 50%, var(--stage-light) 0%, var(--stage) 70%);
    font-family: "Roboto", Arial, sans-serif;
    color: var(--white);
  }
  .page-header {
    position: absolute; top: 0; left: 0; width: 1200px; height: 63px;
    background: var(--brand-blue);
    box-shadow: 0 2px 3px rgba(0,0,0,.35);
    display: flex; align-items: center; justify-content: center;
  }
  .page-title { font-size: 35px; font-weight: 400; letter-spacing: .3px; }
  .page-footer {
    position: absolute; left: 0; bottom: 0; width: 1200px; height: 12px;
    background: var(--brand-blue);
  }
  .banner-label { position: absolute; font-size: 18px; font-weight: 400; }
  .banner {
    position: absolute; width: 250px; height: 250px; overflow: hidden;
    box-shadow: 3px 4px 6px rgba(0,0,0,.45);
  }
  .banner-art { position: absolute; inset: 0; width: 250px; height: 250px; display: block; }

  /* Banner 1 */
  .brand-name {
    position: absolute; top: 4px; left: 0; width: 250px; text-align: center;
    font-family: "Roboto Slab", Georgia, serif; font-weight: 700; font-size: 30px;
    color: var(--brand-blue); letter-spacing: .5px;
  }
  .slogan {
    position: absolute; top: 48px; left: 0; width: 250px; text-align: center;
    font-family: "Roboto Slab", Georgia, serif; font-weight: 700; font-size: 12.5px;
    line-height: 17px; color: var(--ink-grey); letter-spacing: .3px;
  }
  .banner-url {
    position: absolute; left: 0; bottom: 0; width: 250px; height: 31px;
    display: flex; align-items: center; justify-content: center;
    font-family: "Roboto Slab", Georgia, serif; font-size: 17px; color: var(--brand-blue);
  }

  /* Lists */
  .feature-list { position: absolute; list-style: none; }
  .feature-list li { display: flex; align-items: flex-start; }
  .tick { flex: none; }
  .feature-list--courses {
    top: 40px; left: 17px; width: 220px;
    font-family: "Open Sans", Arial, sans-serif; font-size: 17.5px; line-height: 21px;
  }
  .feature-list--courses li { margin-bottom: 16px; }
  .feature-list--courses .tick { width: 16px; height: 16px; margin: 3px 9px 0 0; }
  .banner-frame { position: absolute; inset: 6px; border: 1px solid rgba(255,255,255,.45); }
  .feature-list--advanced {
    top: 113px; left: 16px; width: 228px;
    font-family: "Lato", Arial, sans-serif; font-size: 14px; line-height: 17px; letter-spacing: -.2px;
  }
  .feature-list--advanced li { margin-bottom: 8px; }
  .feature-list--advanced .tick { width: 14px; height: 14px; margin: 2px 7px 0 0; }

  /* Banner 4 */
  .contact {
    position: absolute; left: 0; top: 182px; width: 250px; text-align: center;
    font-family: "Roboto", Arial, sans-serif;
  }
  .contact-url { font-size: 23px; line-height: 28px; }
  .contact-phone { font-size: 21px; line-height: 28px; }
</style>
</head>
<body>
  <header class="page-header"><h1 class="page-title">Torvenix Banners</h1></header>

  <!-- Banner 1 -->
  <div class="banner-label" style="left:325px; top:194px;">Banner-1</div>
  <section class="banner" style="left:325px; top:235px;">
    <svg class="banner-art" viewBox="0 0 250 250">
      <defs>
        <linearGradient id="b1photo" x1="0" y1="0" x2="0" y2="1">
          <stop offset="0" stop-color="#c9d6dd"/>
          <stop offset=".45" stop-color="#6f8fa6"/>
          <stop offset=".7" stop-color="#4f8a3a"/>
          <stop offset="1" stop-color="#3d6a2e"/>
        </linearGradient>
      </defs>
      <rect width="250" height="250" fill="#ffffff"/>
      <rect y="60" width="250" height="158" fill="url(#b1photo)" role="img" aria-label="Photo of two instructors standing beside a white helicopter on a grass airfield"/>
      <path d="M0,0 H250 V62 Q125,122 0,62 Z" fill="#ffffff"/>
      <path d="M0,62 Q125,122 250,62 V69 Q125,129 0,69 Z" fill="var(--brand-blue)"/>
      <rect y="217" width="250" height="1.5" fill="#222"/>
      <rect y="218.5" width="250" height="31.5" fill="#ffffff"/>
    </svg>
    <div class="brand-name">Torvenix</div>
    <p class="slogan">AFFORDABLE. ACCELERATED.<br>EFFECTIVE</p>
    <div class="banner-url">www.torvenix.com</div>
  </section>

  <!-- Banner 2 -->
  <div class="banner-label" style="left:651px; top:194px;">Banner-2</div>
  <section class="banner" style="left:651px; top:235px;">
    <svg class="banner-art" viewBox="0 0 250 250" role="img" aria-label="Photo of an instructor in a classroom under a blue tint">
      <defs>
        <linearGradient id="b2photo" x1="0" y1="0" x2="1" y2="1">
          <stop offset="0" stop-color="#1a78bd"/>
          <stop offset=".6" stop-color="#2a82c2"/>
          <stop offset="1" stop-color="#1569a9"/>
        </linearGradient>
      </defs>
      <rect width="250" height="250" fill="url(#b2photo)"/>
    </svg>
    <div class="banner-frame"></div>
    <ul class="feature-list feature-list--courses">
      <li><svg class="tick" viewBox="0 0 16 16"><circle cx="8" cy="8" r="8" fill="#e6eef5"/><path d="M4.3 8.2 L7 10.8 L11.8 5.6" fill="none" stroke="#1077bf" stroke-width="1.8"/></svg><span>Accelerated Training Courses</span></li>
      <li><svg class="tick" viewBox="0 0 16 16"><circle cx="8" cy="8" r="8" fill="#e6eef5"/><path d="M4.3 8.2 L7 10.8 L11.8 5.6" fill="none" stroke="#1077bf" stroke-width="1.8"/></svg><span>Private Pilot in 4-weeks</span></li>
      <li><svg class="tick" viewBox="0 0 16 16"><circle cx="8" cy="8" r="8" fill="#e6eef5"/><path d="M4.3 8.2 L7 10.8 L11.8 5.6" fill="none" stroke="#1077bf" stroke-width="1.8"/></svg><span>Career Programs from PPL to CFII</span></li>
      <li><svg class="tick" viewBox="0 0 16 16"><circle cx="8" cy="8" r="8" fill="#e6eef5"/><path d="M4.3 8.2 L7 10.8 L11.8 5.6" fill="none" stroke="#1077bf" stroke-width="1.8"/></svg><span>Pay-as-you-go</span></li>
    </ul>
  </section>

  <!-- Banner 3 -->
  <div class="banner-label" style="left:325px; top:538px;">Banner-3</div>
  <section class="banner" style="left:325px; top:578px;">
    <svg class="banner-art" viewBox="0 0 250 250">
      <defs>
        <linearGradient id="b3photo" x1="0" y1="0" x2="0" y2="1">
          <stop offset="0" stop-color="#3f82c4"/>
          <stop offset=".55" stop-color="#cfe0ee"/>
          <stop offset="1" stop-color="#5b8f3f"/>
        </linearGradient>
      </defs>
      <rect width="250" height="150" fill="url(#b3photo)" role="img" aria-label="Photo of a white helicopter flying low over a field under a cloudy sky"/>
      <path d="M0,97 C40,70 100,60 140,74 C185,90 200,140 250,140 V250 H0 Z" fill="#ffffff"/>
      <path d="M0,102 C40,76 100,66 138,80 C182,96 198,146 250,146 V250 H0 Z" fill="var(--brand-blue)"/>
    </svg>
    <ul class="feature-list feature-list--advanced">
      <li><svg class="tick" viewBox="0 0 16 16"><circle cx="8" cy="8" r="8" fill="#e6eef5"/><path d="M4.3 8.2 L7 10.8 L11.8 5.6" fill="none" stroke="#1077bf" stroke-width="1.8"/></svg><span>Advanced Training</span></li>
      <li><svg class="tick" viewBox="0 0 16 16"><circle cx="8" cy="8" r="8" fill="#e6eef5"/><path d="M4.3 8.2 L7 10.8 L11.8 5.6" fill="none" stroke="#1077bf" stroke-width="1.8"/></svg><span>Firefighting (QPRA) &amp; Forestry Tactics Training</span></li>
      <li><svg class="tick" viewBox="0 0 16 16"><circle cx="8" cy="8" r="8" fill="#e6eef5"/><path d="M4.3 8.2 L7 10.8 L11.8 5.6" fill="none" stroke="#1077bf" stroke-width="1.8"/></svg><span>KX 310 &amp; Tarn 118K Turbine Transition Training</span></li>
      <li><svg class="tick" viewBox="0 0 16 16"><circle cx="8" cy="8" r="8" fill="#e6eef5"/><path d="M4.3 8.2 L7 10.8 L11.8 5.6" fill="none" stroke="#1077bf" stroke-width="1.8"/></svg><span>External-Load (VR) Courses</span></li>
    </ul>
  </section>

  <!-- Banner 4 -->
  <div class="banner-label" style="left:651px; top:538px;">Banner-4</div>
  <section class="banner" style="left:651px; top:578px;">
    <svg class="banner-art" viewBox="0 0 250 250">
      <defs>
        <linearGradient id="b4photo" x1="0" y1="0" x2="1" y2="1">
          <stop offset="0" stop-color="#2d4f6b"/>
          <stop offset=".5" stop-color="#7fa6c6"/>
          <stop offset="1" stop-color="#d9e6ef"/>
        </linearGradient>
      </defs>
      <rect width="250" height="200" fill="url(#b4photo)" role="img" aria-label="Photo of a helmeted pilot leaning out of a helicopter door against a bright sky"/>
      <path d="M0,176 L204,116 L250,150 V250 H0 Z" fill="#ffffff"/>
      <path d="M0,183 L204,124 L250,160 V250 H0 Z" fill="var(--brand-blue)"/>
    </svg>
    <div class="contact">
      <div class="contact-url">www.torvenix.com</div>
      <div class="contact-phone">Call: (555) 482-7093</div>
    </div>
  </section>

  <footer class="page-footer"></footer>
</body>
</html>
```